Tradeshow Booth Design

Clean background, some variance of kelly green in the colors - see image for text - maybe an image with people or nice modern homes...

Target Market(s)

Mortgage Professionals

Industry/Entity Type

Mortgage Lender

Font styles to use
Serif
Sans Serif

Colors
9bcb3c
cadf82

Requirements
Must have
• Logo, the words on the image

```html
<!DOCTYPE html>
<html lang="en">
<head>
<meta charset="utf-8">
<title>Birchline Lending – Tradeshow Booth</title>
<link rel="stylesheet" href="https://fonts.googleapis.com/css2?family=Montserrat:wght@300;700;800&display=swap">
<style>
  :root {
    --kelly-green: #1e6b3a;
    --orange: #f7941d;
    --pale-orange: #fdcb6e;
    --grey-text: #a7a9ac;
    --grey-rule: #bcbec0;
    --floor: #e6e7e8;
    --floor-edge: #c7c8ca;
    --trim-guide: #e2403a;
    --white: #ffffff;
  }
  html, body {
    margin: 0;
    padding: 0;
    width: 1200px;
    height: 800px;
    overflow: hidden;
    background: var(--white);
  }
  .booth {
    position: relative;
    width: 1200px;
    height: 800px;
    overflow: hidden;
    font-family: "Montserrat", Arial, sans-serif;
    line-height: 1;
  }
  .booth__art {
    position: absolute;
    inset: 0;
  }
  .brand-name {
    position: absolute;
    left: 453px;
    top: 62px;
    margin: 0;
    font-size: 49px;
    font-weight: 700;
    color: var(--white);
    letter-spacing: 0.5px;
    white-space: nowrap;
  }
  .tagline {
    position: absolute;
    right: 205px;
    top: 201px;
    margin: 0;
    text-align: right;
    color: var(--grey-text);
  }
  .tagline__strong {
    display: block;
    font-size: 33px;
    font-weight: 800;
    letter-spacing: 0.5px;
  }
  .tagline__light {
    display: block;
    margin-top: 3px;
    font-size: 41px;
    font-weight: 300;
  }
  .headline {
    position: absolute;
    left: 231px;
    top: 332px;
    margin: 0;
    color: var(--kelly-green);
    font-weight: normal;
  }
  .headline__lead {
    display: block;
    font-size: 52px;
    font-weight: 700;
  }
  .headline__main {
    display: block;
    margin-top: 3px;
    font-size: 62px;
    font-weight: 300;
    white-space: nowrap;
  }
  .headline__for {
    font-size: 32px;
    margin-left: 8px;
  }
  .audience {
    position: absolute;
    left: 231px;
    top: 461px;
    margin: 0;
    color: var(--orange);
    font-size: 32px;
    font-weight: 800;
    line-height: 37px;
    letter-spacing: 0.3px;
  }
</style>
</head>
<body>
<main class="booth">
  <svg class="booth__art" width="1200" height="800" viewBox="0 0 1200 800" aria-hidden="true">
    <path class="header-band" fill="var(--kelly-green)"
          d="M0 0 H1200 V155 C1080,143 960,136 840,137 C560,140 230,240 0,414 Z"/>
    <path class="accent-pale" fill="var(--pale-orange)"
          d="M0 414 C230,240 560,140 840,137 C560,148 250,270 0,459 Z"/>
    <path class="accent-orange" fill="var(--orange)"
          d="M0 414 C230,240 560,140 840,137 C560,144 240,258 0,442 Z"/>
    <circle class="brand-dot" cx="352" cy="98" r="52" fill="var(--white)"/>
    <line class="rule rule--tagline" x1="729" y1="284" x2="995" y2="284" stroke="var(--grey-rule)" stroke-width="1.5"/>
    <line class="rule rule--headline" x1="231" y1="454.5" x2="670" y2="454.5" stroke="var(--grey-rule)" stroke-width="1.5"/>
    <rect class="floor" x="0" y="763" width="1200" height="37" fill="var(--floor)"/>
    <rect class="floor-edge" x="0" y="763" width="1200" height="4" fill="var(--floor-edge)"/>
    <line class="trim-guide" x1="155" y1="0" x2="155" y2="800" stroke="var(--trim-guide)" stroke-width="1" stroke-dasharray="9 6"/>
    <line class="trim-guide" x1="1045" y1="0" x2="1045" y2="800" stroke="var(--trim-guide)" stroke-width="1" stroke-dasharray="9 6"/>
  </svg>

  <p class="brand-name">BIRCHLINE LENDING</p>

  <p class="tagline">
    <span class="tagline__strong">FLEXIBLE</span>
    <span class="tagline__light">GUIDELINES</span>
  </p>

  <h1 class="headline">
    <span class="headline__lead">Innovative</span>
    <span class="headline__main">SOLUTIONS<span class="headline__for">for</span></span>
  </h1>

  <p class="audience">NON-TRADITIONAL<br>BORROWERS</p>
</main>
</body>
</html>
```